Church Bulletin Ad (see attached sample)

Create a New Church Bulletin Ad. I have attached some samples of what we would like to have in the ad. (1) Ferrowind Realty Ostra Logo (2) Headshot (3) Lorna Vesk & Greta Vesk, Real Estate Team (4) Phone number (5) Email address (6) St Adela Parishioners for over 40 Years. We would like for the ad to be clean and modern. NO OTHER IMAGES besides headshots and Ferrowind Realty Ostra Logo.

Target Market(s)

Church community

Industry/Entity Type

Real Estate

Font styles to use
Sans Serif
Other font styles liked:
• Modern Font

Colors
0054AA
0677BA
7BADD7
CADEEF
E8F1F8

Requirements
Must have
• Ferrowind Realty Ostra Logo; Headshot; Ad size is 4.5"x1.62"

```html
<!DOCTYPE html>
<html lang="en">
<head>
<meta charset="utf-8">
<title>Vesk Marlow Real Estate Team – Bulletin Ad</title>
<link href="https://fonts.googleapis.com/css2?family=Josefin+Sans:wght@400;700&family=Kanit:ital,wght@1,600&family=Tinos:ital,wght@1,700&display=swap" rel="stylesheet">
<style>
  :root {
    --brand-blue: #0054AA;
    --brand-navy: #122E6B;
    --accent-blue: #1AA3E0;
    --banner-blue: #7BADD7;
    --paper: #E8E9EB;
    --ink: #333333;
    --white: #FFFFFF;
  }
  html, body { margin: 0; padding: 0; overflow: hidden; background: var(--white); }
  .ad {
    position: relative;
    width: 1200px;
    height: 427px;
    overflow: hidden;
    background: var(--paper);
    font-family: "Josefin Sans", sans-serif;
    color: var(--ink);
  }
  .top-band {
    position: absolute; left: 0; top: 0;
    width: 1200px; height: 112px;
    background: var(--brand-blue);
  }
  .headline {
    position: absolute; left: 224px; top: 14px;
    width: 940px; height: 80px;
    margin: 0;
  }
  .headline svg { display: block; overflow: visible; }
  .headline text {
    font-family: "Kanit", sans-serif;
    font-style: italic; font-weight: 600;
    font-size: 66px;
    fill: var(--white);
  }
  .logo-frame {
    position: absolute; left: 45px; top: 16px;
    width: 139px; height: 127px;
    background: var(--white);
    box-shadow: 0 2px 4px rgba(0,0,0,.25);
  }
  .logo-mark {
    position: absolute; left: 9px; top: 8px;
    width: 121px; height: 111px;
    background: var(--brand-navy);
    display: flex; align-items: center; justify-content: center;
    text-align: center;
    color: var(--white);
    font-weight: 700; font-size: 17px; line-height: 21px;
    padding: 0 8px; box-sizing: border-box;
  }
  .headshot { position: absolute; }
  .headshot--left {
    left: 0; top: 144px; width: 250px; height: 283px;
    border-radius: 110px 110px 0 0;
    background: linear-gradient(180deg, #5a3b2a 0%, #8a6a58 45%, #2a2226 100%);
  }
  .headshot--right {
    left: 932px; top: 140px; width: 268px; height: 287px;
    border-radius: 120px 120px 0 0;
    background: linear-gradient(180deg, #e4e1dc 0%, #c9a99a 45%, #2b2725 100%);
  }
  .team-name {
    position: absolute; left: 230px; top: 134px;
    margin: 0;
    font-weight: 700; font-size: 40px; line-height: 46px;
    letter-spacing: 1.2px;
    white-space: nowrap;
  }
  .team-role {
    position: absolute; left: 230px; top: 184px;
    margin: 0;
    font-weight: 400; font-size: 37px; line-height: 42px;
    letter-spacing: 1.5px;
    white-space: nowrap;
  }
  .contact {
    position: absolute; left: 288px; top: 258px;
    margin: 0; padding: 0; list-style: none;
    font-size: 31px; line-height: 32px;
  }
  .contact li { display: flex; align-items: center; height: 32px; margin-bottom: 14px; white-space: nowrap; }
  .contact svg { margin-right: 12px; flex: none; }
  .tagline-banner {
    position: absolute; left: 234px; top: 357px;
    width: 732px; height: 70px;
    background: var(--banner-blue);
    border-radius: 10px 10px 0 0;
  }
  .tagline {
    position: absolute; left: 25px; top: 13px;
    margin: 0;
    font-family: "Tinos", serif;
    font-style: italic; font-weight: 700;
    font-size: 39px; line-height: 42px;
    color: var(--ink);
    white-space: nowrap;
  }
</style>
</head>
<body>
<main class="ad">
  <div class="top-band"></div>
  <h1 class="headline">
    <svg width="940" height="80" viewBox="0 0 940 80">
      <text x="2" y="66" textLength="934" lengthAdjust="spacingAndGlyphs">ENERGY EXCELLENCE EXPERIENCE</text>
    </svg>
  </h1>

  <div class="logo-frame">
    <div class="logo-mark">Ferrowind Realty Ostra</div>
  </div>

  <div class="headshot headshot--left" role="img" aria-label="Headshot of Lorna Vesk Marlow"></div>
  <div class="headshot headshot--right" role="img" aria-label="Headshot of Greta Vesk"></div>

  <h2 class="team-name">Lorna Vesk Marlow &amp; Greta Vesk</h2>
  <p class="team-role">Real Estate Team</p>

  <ul class="contact">
    <li>
      <svg width="26" height="26" viewBox="0 0 24 24" aria-hidden="true">
        <path fill="#1AA3E0" d="M20 2.5c-.8-.6-2-.4-2.6.4l-1.6 2.4c-.5.8-.3 1.8.4 2.4l1 .8c-.9 3.3-3.2 6.6-6.2 8.6l-1-.7c-.8-.5-1.8-.4-2.4.3l-1.8 2.2c-.6.8-.5 1.9.3 2.5l1 .8c5.8-1.7 12.6-10.5 13.900-17l-1-.7z"/>
      </svg>
      <span>(206) 555-0148</span>
    </li>
    <li>
      <svg width="26" height="20" viewBox="0 0 26 20" aria-hidden="true">
        <rect x="0" y="0" width="26" height="20" rx="2" fill="#1AA3E0"/>
        <path d="M2 3l11 8 11-8" fill="none" stroke="#FFFFFF" stroke-width="2"/>
      </svg>
      <span>veskMarlowTeam@ferrowind.com</span>
    </li>
  </ul>

  <div class="tagline-banner">
    <p class="tagline">St Adela Parishioners for over 40 Years</p>
  </div>
</main>
</body>
</html>
```